We are looking for a 2-page (front and back) 3.67" x 8.5" rack card. . Please refer back to our other Rack Cards for a similar look and feel to the card. This one is titled: Myths and Truths About Memory Loss
The document is for older readers. Do not put text over graphics and keep it simple and easy to read with high contrast.
We want some very simple design element(s) incorporated that convey Native American communities or heritage. But NO headdress, teepee graphics, owls etc. I have included some graphics, please use your creative discretion to use which ones look good on the cards. Please remember to include the funding statement - it can be in a very small font 6/7 point. For more information about our project, please visit https://orvelmesa.net/mind-care/library - This rack card is supported by the Bureau for Wellness Tracking and Outreach (BWT) of the Federal Office of Family and Care Affairs (FOF) as part of a financial assistance award totaling $1,053,119.36 with 100 percent funded by BWT/FOF. The contents are those of the author(s) and do not necessarily represent the official views of, nor an endorsement, by BWT/FOF, or the U.S. Government.
Please feel free to choose one of each of the 2 logos that looks best. We have the QT7 logo and the Mind Wellness Support Hub logo we would like to add. I have added the document and there are images to choose from to use in the rack card. We definitely want to incorporate the coyote in this rack card since it is culturally significant.

```html
<!DOCTYPE html>
<html lang="en">
<head>
<meta charset="utf-8">
<title>Myths and Truths About Memory Loss – Rack Card</title>
<link rel="stylesheet" href="https://fonts.googleapis.com/css2?family=Oswald:wght@500;600&family=Poppins:ital,wght@0,400;0,500;0,600;0,700;0,800;1,400;1,500;1,600&display=swap">
<style>
:root{
  --bg:#353e42;
  --teal:#4aa3ab;
  --red:#b05a52;
  --ink:#2b1616;
  --rule:#6fb6bc;
  --chip:#e4e4e4;
  --white:#ffffff;
}
*{box-sizing:border-box;margin:0;padding:0}
html,body{width:1200px;height:1200px;overflow:hidden;background:var(--bg)}
.stage{position:absolute;left:0;top:0;width:1932px;height:1932px;transform:scale(0.62112);transform-origin:0 0;font-family:"Poppins",sans-serif;color:var(--ink)}
.card{position:absolute;top:174px;width:684px;height:1586px;background:var(--white);overflow:hidden;box-shadow:0 4px 14px rgba(0,0,0,.25)}
.card--front{left:263px}
.card--back{left:986px}

/* header */
.brand{position:absolute;left:57px;top:40px;display:flex;align-items:center;gap:26px}
.brand__mark{width:100px;height:100px;background:var(--teal)}
.brand__name{font-family:"Oswald",sans-serif;font-weight:600;color:var(--red);font-size:40px;line-height:1.08;letter-spacing:.5px;text-transform:uppercase}

.photo{position:absolute;left:0;top:167px;width:684px;height:288px}
.photo--front{background:linear-gradient(100deg,#7d5a44 0%,#4e7d92 45%,#3e6f80 70%,#8a8f86 100%)}
.photo--back{background:linear-gradient(90deg,#6d7a4f 0%,#9a8a78 35%,#8b6a5a 60%,#5a7ea8 100%)}
.band{position:absolute;left:0;top:455px;width:684px;height:28px;background:linear-gradient(180deg,#9ccacd 0%,#c9a29c 100%)}

/* front title */
.title{position:absolute;left:0;width:684px;top:512px;text-align:center;font-weight:800;font-size:52px;line-height:54px;letter-spacing:.5px}
.title .t{color:var(--teal)}.title .r{color:var(--red)}
.intro{position:absolute;left:52px;width:580px;top:642px;text-align:center;font-size:20px;line-height:25px;letter-spacing:-.3px}

/* myth list */
.mt{font-size:17px;line-height:21.5px;letter-spacing:-.25px}
.mt__row{padding-left:67px;text-indent:-67px;margin-bottom:6px}
.mt__row--flow{padding-left:0;text-indent:0}
.mt__label{display:inline-block;width:67px;text-indent:0;font-size:19px}
.mt__label--myth{color:var(--teal)}
.mt__label--truth{color:var(--red)}
.mt__text--truth{font-weight:500}
.mt__item{padding:9px 0 8px}
.mt__item + .mt__item{border-top:1.5px solid var(--rule)}

.box-front{position:absolute;left:53px;top:845px;width:578px;height:230px;border:2px solid var(--teal);border-bottom:0;border-radius:26px 26px 0 0}
.box-front__dots{position:absolute;left:53px;top:1075px;width:578px;height:90px;border-left:2px dotted var(--teal);border-right:2px dotted var(--teal)}
.box-front__head{position:absolute;left:0;width:684px;top:820px;text-align:center;line-height:50px}
.box-front__head .wrap{background:var(--white);padding:0 16px;font-weight:800;font-size:40px;color:var(--teal)}
.box-front__head .vs{color:var(--ink)}.box-front__head .tr{color:var(--red)}
.list-front{position:absolute;left:73px;width:532px;top:880px}

/* hub */
.hub{position:absolute;display:flex;align-items:center;gap:12px}
.hub__dot{width:70px;height:70px;border-radius:50%;background:var(--teal)}
.hub__name{font-weight:600;color:var(--teal);font-size:19px;line-height:21px;text-transform:uppercase}

/* quote */
.foot-grad{position:absolute;left:0;top:1405px;width:684px;height:181px;background:linear-gradient(90deg,#b5574f 0%,#8e8a88 55%,#4aa6ad 100%)}
.quote{position:absolute;left:53px;top:1305px;width:578px;height:193px;background:var(--white);border:2px solid var(--red);border-radius:26px;text-align:center;padding-top:18px}
.quote__text{font-weight:600;font-size:21px;line-height:26px;padding:0 62px}
.quote__mark{position:absolute;font-weight:700;font-size:48px;line-height:1;color:var(--ink)}
.quote__who{margin-top:14px;font-style:italic;font-size:25px;font-weight:600}
.quote__who span{font-weight:400}
.quote__role{font-style:italic;font-size:19px}
.web{position:absolute;display:flex;align-items:center;gap:14px;font-size:36px}
.web b{font-weight:700}
.web--front{left:130px;top:1515px;color:var(--white)}
.web--back{left:176px;top:1463px;font-size:29px;color:var(--red)}

/* back */
.box-back-dots{position:absolute;left:53px;top:520px;width:578px;height:80px;border-left:2px dotted var(--teal);border-right:2px dotted var(--teal)}
.box-back{position:absolute;left:53px;top:600px;width:578px;height:264px;border:2px solid var(--teal);border-top:0;border-radius:0 0 26px 26px}
.list-back{position:absolute;left:73px;width:538px;top:510px}
.h2{position:absolute;left:0;width:684px;top:885px;text-align:center;font-weight:800;font-size:40px;color:var(--teal)}
.act{position:absolute;left:50px;width:584px;top:946px;text-align:center;font-size:20px;line-height:25px;letter-spacing:-.3px}

.res{position:absolute;left:53px;top:1150px;width:578px;height:300px;border:2px solid var(--red);border-radius:26px;text-align:center;padding:12px 20px 0}
.res__head{font-weight:600;font-size:20px;margin-bottom:12px}
.res__label{font-size:16px;margin-bottom:5px}
.res__url{background:var(--chip);font-size:14.5px;line-height:21px;padding:5px 6px;margin-bottom:10px;letter-spacing:-.2px}
.fund{position:absolute;left:52px;width:580px;top:1520px;text-align:center;font-style:italic;font-size:8.6px;line-height:11px}
</style>
</head>
<body>
<div class="stage">

  <!-- FRONT -->
  <section class="card card--front">
    <header class="brand">
      <div class="brand__mark"></div>
      <div class="brand__name">QT7 · Native Elder<br>Wellness Alliance</div>
    </header>
    <div class="photo photo--front" role="img" aria-label="Photo of a smiling Elder holding two young grandchildren, beside a smoking sage bundle in an abalone shell"></div>
    <div class="band" role="img" aria-label="Woven zigzag border pattern in teal and red"></div>

    <h1 class="title"><span class="t">MYTHS AND TRUTHS</span><br><span class="r">ABOUT MEMORY LOSS</span></h1>
    <p class="intro">People sometimes believe things about memory loss that are not true. Misunderstandings can make it harder for Elders in Native communities to get the help they need when they start having memory issues. Below are some common myths and truths about memory loss, Alzheimer’s disease, and related dementias.</p>

    <div class="box-front"></div>
    <div class="box-front__dots"></div>
    <h2 class="box-front__head"><span class="wrap">MYTHS <span class="vs">VS</span> <span class="tr">TRUTHS</span></span></h2>

    <div class="list-front mt">
      <div class="mt__item">
        <p class="mt__row"><span class="mt__label mt__label--myth">Myth:</span>Getting Alzheimer’s is a normal part of aging.</p>
        <p class="mt__row mt__text--truth"><span class="mt__label mt__label--truth">Truth:</span>It is a disease that not everyone will get.</p>
      </div>
      <div class="mt__item">
        <p class="mt__row"><span class="mt__label mt__label--myth">Myth:</span>Memory problems and forgetfulness are definite signs of dementia.</p>
        <p class="mt__row mt__text--truth"><span class="mt__label mt__label--truth">Truth:</span>Memory problems do not solely determine if they are dementia. Other medical conditions can cause memory problems. Talk to your doctor.</p>
      </div>
      <div class="mt__item">
        <p class="mt__row"><span class="mt__label mt__label--myth">Myth:</span>Only older people can get Alzheimer’s disease.</p>
        <p class="mt__row mt__text--truth"><span class="mt__label mt__label--truth">Truth:</span>There have been cases for people as young as twenty-five, though it is rare to undergo treatment.</p>
      </div>
    </div>

    <div class="hub" style="left:205px;top:1200px">
      <div class="hub__dot"></div>
      <div class="hub__name">Mind Wellness<br>Support Hub</div>
    </div>

    <div class="foot-grad"></div>
    <blockquote class="quote">
      <span class="quote__mark" style="left:20px;top:20px">“</span>
      <p class="quote__text">The beauty in life is each day is a new day to try again and be a better version of myself than yesterday.”</p>
      <span class="quote__mark" style="right:20px;top:68px">”</span>
      <p class="quote__who">Maren Tallgrass <span>(Blackfeet),</span></p>
      <p class="quote__role">personal communication with the author.</p>
    </blockquote>

    <div class="web web--front">
      <svg width="40" height="40" viewBox="0 0 40 40" fill="none" stroke="#fff" stroke-width="3"><circle cx="20" cy="20" r="17"/><ellipse cx="20" cy="20" rx="7" ry="17"/><line x1="3" y1="20" x2="37" y2="20"/></svg>
      <span>www.<b>orvelmesa</b>.net</span>
    </div>
  </section>

  <!-- BACK -->
  <section class="card card--back">
    <header class="brand">
      <div class="brand__mark"></div>
      <div class="brand__name">QT7 · Native Elder<br>Wellness Alliance</div>
    </header>
    <div class="photo photo--back" role="img" aria-label="Collage of Elders outdoors, a talking circle, multicolored corn, dancer regalia and a couple holding a feather fan"></div>
    <div class="band" role="img" aria-label="Woven zigzag border pattern in teal and red"></div>

    <div class="box-back-dots"></div>
    <div class="box-back"></div>
    <div class="list-back mt">
      <div class="mt__item">
        <p class="mt__row"><span class="mt__label mt__label--myth">Myth:</span>People with Alzheimer’s disease cannot be happy.</p>
        <p class="mt__row mt__row--flow mt__text--truth"><span class="mt__label mt__label--truth">Truth:</span>A person with memory loss can experience strong moods and emotions but still enjoy life and relationships.</p>
      </div>
      <div class="mt__item">
        <p class="mt__row"><span class="mt__label mt__label--myth">Myth:</span>Dementia can be prevented by a certain supplement or food.</p>
        <p class="mt__row mt__text--truth"><span class="mt__label mt__label--truth">Truth:</span>Healthy eating may help overall wellness, including brain health. No additional supplements will completely prevent the onset of dementia.</p>
      </div>
      <div class="mt__item">
        <p class="mt__row"><span class="mt__label mt__label--myth">Myth:</span>Alzheimer’s is reversible through prescription drugs.</p>
        <p class="mt__row mt__text--truth"><span class="mt__label mt__label--truth">Truth:</span>There are prescription drugs to address symptoms of Alzheimer’s and dementia, but there are no medicines that can reverse them.</p>
      </div>
    </div>

    <h2 class="h2">WHAT YOU CAN DO</h2>
    <p class="act">If you or someone you love is having memory problems, do not wait. Talk to a healthy provider you trust. Learning the truth can help keep our Elders strong and supported.</p>

    <div class="hub" style="left:205px;top:1052px">
      <div class="hub__dot"></div>
      <div class="hub__name">Mind Wellness<br>Support Hub</div>
    </div>

    <div class="res">
      <p class="res__head">For More Myth-Busting Information:</p>
      <p class="res__label">12 Common Alzheimer's Disease Myths on Carefinder:</p>
      <p class="res__url">https://www.carefinder.example/c/memory-myths-busted/</p>
      <p class="res__label">Memory Care Alliance Myths vs. Facts:</p>
      <p class="res__url">https://www.memorycare.example/dementia/research-and-progress/<br>clinical-trials/myths-vs-facts</p>
      <p class="res__label">QT7 Brain Health Resources</p>
      <p class="res__url">https://orvelmesa.net/resources/</p>
    </div>

    <div class="web web--back">
      <svg width="30" height="30" viewBox="0 0 40 40" fill="none" stroke="#3b8f93" stroke-width="3.5"><circle cx="20" cy="20" r="17"/><ellipse cx="20" cy="20" rx="7" ry="17"/><line x1="3" y1="20" x2="37" y2="20"/></svg>
      <span>www.<b>orvelmesa</b>.net</span>
    </div>

    <p class="fund">For more information about our project, please visit https://orvelmesa.net/mind-care/library - This rack card is supported by the Bureau for Wellness Tracking and Outreach (BWT) of the Federal Office of Family and Care Affairs (FOF) as part of a financial assistance award totaling $1,053,119.36 with 100 percent funded by BWT/FOF. The contents are those of the author(s) and do not necessarily represent the official views of, nor an endorsement, by BWT/FOF, or the U.S. Government.</p>
  </section>

</div>
</body>
</html>
```